Redesign PixelHarbor's Designer Account Home Page

Are a web designer? New to PixelHarbor? This contest is for you!

We want you to redesign PixelHarbor's designer account home page. We're looking for bold and innovative ideas to make this page a useful and fun experience for you and your fellow designers.

Only new registrants this month are eligible to enter this contest and win prizes.

Your task:
* We want you to put your web design skills to the test and re-design the My Account home page ("Overview") on PixelHarbor to make it more functional and engaging for designers on PixelHarbor.
* The page you are redesigning is here: http://www.pixelharbor-example.com/my-profile.
* Your design should allow for the same functionality as the existing page, though you don't need to replicate the same elements (buttons) or the same menu structure.
* Your design must fit with the branding of the site.
* You must provide a brief outline of what changes you made and why when you upload your design
* 1 submission per designer - make it your best work!
* Pls see "Must haves" for requirements.

Deadline:
* Submit before 12:00am 1st September UTC. Pls convert this deadline to your local timezone and take note of the local time and date

Prizes: $1,000 to win
* First prize for the best design is $700
* Second prize is $200
* Third prize is $100

If you started from scratch, how would you design the MyAccount page on PixelHarbor?

Good luck & have fun!

Mel / The PixelHarbor Team

Target Market(s)

PixelHarbor designers

Number of Pages Required

1 page

Requirements
Must have
• Dimensions: 1200 x 1000 px
• Minimum 150-300 dpi
• Your design must adhere to our quality standards to be eligible to receive a prize
• Submissions must be created in Adobe Creative Suite (Illustrator or Photoshop)
• Your design must fit with the branding of the PixelHarbor site.
• Only new registrants this month are eligible to enter and win prizes.

```html
<!DOCTYPE html>
<html lang="en">
<head>
<meta charset="utf-8">
<title>PixelHarbor – My Account Overview</title>
<link href="https://fonts.googleapis.com/css2?family=Open+Sans:wght@400;600;700&display=swap" rel="stylesheet">
<style>
:root{
  --brand-blue:#2b9ad3;
  --brand-green:#8cc63f;
  --ink:#333333;
  --muted:#8a8a8a;
  --line:#dddddd;
  --page-bg:#e8e8e8;
  --panel:#ffffff;
  --band-dark:#2e2e2e;
  --band-darker:#232323;
  --stats-dark:#3a3a3a;
  --section-blue:#3a8cbd;
  --footer-bg:#2b2b2b;
  --footer-base:#1f1f1f;
  --footer-text:#9a9a9a;
}
*{box-sizing:border-box;margin:0;padding:0}
html,body{width:726px;height:1200px;overflow:hidden}
body{font-family:"Open Sans",Arial,sans-serif;color:var(--ink);background:var(--page-bg);font-size:8px;position:relative}

/* top header */
.site-header{height:26px;background:#fff;display:flex;align-items:center;padding:0 14px;border-bottom:1px solid #e4e4e4}
.brand{display:flex;align-items:center;gap:4px;font-weight:700;font-size:13px;color:var(--brand-blue)}
.brand-dot{width:9px;height:9px;border-radius:50%;background:var(--brand-blue)}
.main-nav{display:flex;gap:9px;margin-left:16px;font-size:6.5px;color:#666}
.main-nav .phone{margin-left:6px;color:#444}
.flag-chip{width:10px;height:7px;background:#2a3f8f;margin-left:4px;display:inline-block}
.header-right{margin-left:auto;display:flex;gap:6px;align-items:center}
.profile-select{width:70px;height:13px;border:1px solid #ccc;font-size:6.5px;padding:2px 4px;color:#555}
.btn-green{height:13px;padding:0 10px;background:var(--brand-green);color:#fff;font-size:6.5px;font-weight:600;display:flex;align-items:center;border-radius:2px}

.breadcrumb{height:20px;background:#f4f4f4;display:flex;align-items:center;gap:5px;padding:0 44px;font-size:6.5px;color:#777;border-bottom:1px solid #e0e0e0}

/* account nav */
.account-nav{height:74px;background:var(--band-dark);display:flex;justify-content:center}
.account-nav a{width:78px;display:flex;flex-direction:column;align-items:center;justify-content:center;gap:6px;color:#bbb;text-decoration:none;font-size:6.5px}
.account-nav a.active{background:var(--band-darker);color:#fff;border-bottom:3px solid var(--brand-blue)}
.account-nav svg{width:20px;height:20px}

.page-title{text-align:center;font-size:17px;font-weight:600;color:#444;padding:34px 0 22px}

.container{width:638px;margin:0 auto}

/* stats */
.stats{height:48px;background:var(--stats-dark);display:flex;align-items:stretch;color:#fff}
.avatar{width:56px;background:#555;display:flex;align-items:center;justify-content:center}
.stat{flex:1;display:flex;align-items:center;gap:8px;padding:0 10px;border-left:1px solid #4c4c4c}
.stat-label{font-weight:700;font-size:9px;color:var(--brand-blue)}
.stat-value{font-size:12px;font-weight:700;line-height:1}
.stat-note{font-size:5.5px;color:#aaa;margin-top:2px}

/* getting started */
.panel{background:var(--panel);border:1px solid var(--line)}
.getting-started{margin-top:24px;height:326px;padding:14px 14px}
.gs-head{display:flex;justify-content:space-between;align-items:baseline}
.gs-title{font-size:11px;font-weight:600}
.gs-percent{font-size:7px;color:#666}
.progress{margin-top:10px;height:22px;background:#d5d5d5;border:1px solid #bcbcbc}
.progress-fill{width:57%;height:100%;background:#3a3a3a}
.todo-heading{font-size:7px;color:#555;margin:8px 0 6px}
.todo{list-style:none}
.todo li{height:31px;border:1px solid #e2e2e2;margin-bottom:3px;display:flex;align-items:center;padding:0 8px;font-size:7px;gap:6px}
.check{width:7px;height:7px;border:1px solid #888;display:flex;align-items:center;justify-content:center}
.check.done{background:#555;border-color:#555}
.todo .action{margin-left:auto}
.btn-complete{background:#333;color:#fff;font-size:6px;padding:3px 9px;border-radius:2px}

/* lower columns */
.columns{display:flex;gap:14px;margin-top:18px}
.col{flex:1;height:246px}
.section-head{height:20px;background:var(--section-blue);color:#fff;font-size:8.5px;font-weight:600;display:flex;align-items:center;padding:0 10px}
.section-intro{font-size:6px;color:#666;padding:7px 10px 4px}
.job{display:flex;gap:7px;padding:7px 10px;border-bottom:1px solid #eee}
.job-dot{width:8px;height:8px;border-radius:50%;background:var(--brand-blue);margin-top:2px;flex:none}
.job-title{font-size:6.2px;color:var(--section-blue)}
.job-meta{font-size:5.5px;color:var(--muted);margin-top:2px}
.pager{display:flex;justify-content:space-between;padding:8px 10px;font-size:6px;color:#555}
.pager span b{background:#eee;border:1px solid #ccc;padding:1px 4px;font-weight:400}
.achievement{display:flex;gap:8px;align-items:center;padding:7px 10px}
.badge{width:20px;height:20px;border-radius:50%;background:#555;border:2px solid #bbb;flex:none}
.ach-title{font-size:6.5px;font-weight:600;color:var(--section-blue)}
.ach-note{font-size:5.5px;color:var(--muted)}

/* footer */
.site-footer{position:absolute;left:0;top:900px;width:726px;height:300px;background:var(--footer-bg);color:var(--footer-text)}
.footer-inner{display:flex;gap:16px;padding:22px 44px 0}
.footer-col h4{color:#fff;font-size:8px;margin-bottom:10px}
.footer-col ul{list-style:none}
.footer-col li{font-size:5.8px;line-height:14px}
.footer-col.links{width:78px}
.tags{display:flex;flex-wrap:wrap;gap:4px;width:130px}
.tags span{background:#3d3d3d;border:1px solid #4a4a4a;color:#ccc;font-size:5.5px;padding:2px 5px;border-radius:2px}
.subscribe{margin-left:auto;width:118px}
.subscribe-field{display:flex;height:13px;margin-bottom:10px}
.subscribe-field div{flex:1;background:#fff}
.subscribe-field span{width:16px;background:var(--brand-green)}
.social{display:flex;gap:6px;margin-bottom:10px}
.social i{width:15px;height:15px;border-radius:50%;background:#555;display:block}
.flags{display:flex;gap:5px;margin-bottom:12px}
.flags i{width:14px;height:9px;background:#4a4a4a;display:block}
.footer-brand{display:flex;align-items:center;gap:4px;color:#fff;font-weight:700;font-size:11px}
.footer-brand i{width:8px;height:8px;background:#fff;border-radius:50%}
.footer-base{position:absolute;bottom:0;left:0;width:100%;height:28px;background:var(--footer-base);font-size:5.5px;display:flex;align-items:center;justify-content:center;color:#777}
</style>
</head>
<body>

<header class="site-header">
  <div class="brand"><span class="brand-dot"></span>PixelHarbor</div>
  <nav class="main-nav">
    <span>Categories</span><span>Designers</span><span>Browse Jobs</span><span>How it works</span>
    <span class="phone">1800 555 0142<span class="flag-chip"></span></span>
  </nav>
  <div class="header-right">
    <div class="profile-select">My Profile ▾</div>
    <div class="btn-green">Member Jobs</div>
  </div>
</header>

<div class="breadcrumb">
  <svg width="8" height="8" viewBox="0 0 10 10"><path d="M1 5 5 1l4 4v4H6V6H4v3H1z" fill="#888"/></svg>
  <span>Home</span><span>›</span><span>My Profile</span>
</div>

<nav class="account-nav">
  <a class="active"><svg viewBox="0 0 20 20"><rect x="3" y="3" width="14" height="14" fill="none" stroke="#fff" stroke-width="2"/><path d="M6 8h8M6 12h8" stroke="#fff" stroke-width="1.5"/></svg>Overview</a>
  <a><svg viewBox="0 0 20 20"><path d="M10 3a5 5 0 0 1 5 5v4l2 2H3l2-2V8a5 5 0 0 1 5-5zM8 16h4a2 2 0 0 1-4 0z" fill="#ccc"/></svg>Notifications</a>
  <a><svg viewBox="0 0 20 20"><circle cx="10" cy="7" r="4" fill="#ccc"/><path d="M3 18a7 6 0 0 1 14 0z" fill="#ccc"/></svg>Profile</a>
  <a><svg viewBox="0 0 20 20"><rect x="2" y="4" width="16" height="12" fill="none" stroke="#ccc" stroke-width="2"/><path d="M4 14l4-5 3 3 2-2 3 4z" fill="#ccc"/></svg>Submissions</a>
  <a><svg viewBox="0 0 20 20"><rect x="2" y="5" width="16" height="11" fill="#ccc"/><path d="M2 5l8 6 8-6" fill="none" stroke="#2e2e2e" stroke-width="1.5"/></svg>Messages</a>
  <a><svg viewBox="0 0 20 20"><path d="M1 10q9-9 18 0-9 9-18 0z" fill="#ccc"/><circle cx="10" cy="10" r="3" fill="#2e2e2e"/></svg>Watchlist</a>
  <a><svg viewBox="0 0 20 20"><rect x="3" y="3" width="6" height="6" fill="#ccc"/><rect x="11" y="3" width="6" height="6" fill="#ccc"/><rect x="3" y="11" width="6" height="6" fill="#ccc"/><rect x="11" y="11" width="6" height="6" fill="#ccc"/></svg>Widgets</a>
  <a><svg viewBox="0 0 20 20"><path d="M3 5h14M3 10h14M3 15h14" stroke="#ccc" stroke-width="2.5"/></svg>My Details</a>
</nav>

<h1 class="page-title">Overview</h1>

<main class="container">
  <section class="stats">
    <div class="avatar"><svg width="24" height="24" viewBox="0 0 20 20"><circle cx="10" cy="7" r="4" fill="#999"/><path d="M3 18a7 6 0 0 1 14 0z" fill="#999"/></svg></div>
    <div class="stat"><span class="stat-label">Rank</span><div><div class="stat-value">#438171</div><div class="stat-note">of 475,127 designers</div></div></div>
    <div class="stat"><span class="stat-label">Position</span><div><div class="stat-value">0%</div><div class="stat-note">(0 of 12 entries)</div></div></div>
    <div class="stat"><span class="stat-label">Submissions</span><div><div class="stat-value">0</div><div class="stat-note">(on average: 0)</div></div></div>
    <div class="stat"><span class="stat-label">Earnings</span><div><div class="stat-value">$0.00</div><div class="stat-note">this year: $0.00 total</div></div></div>
  </section>

  <section class="panel getting-started">
    <div class="gs-head"><h2 class="gs-title">Getting Started - Complete Your Profile</h2><span class="gs-percent">57% Completed</span></div>
    <div class="progress"><div class="progress-fill"></div></div>
    <p class="todo-heading">Things left to do:</p>
    <ul class="todo">
      <li><span class="check done"></span>Tell us what type of designer you are<span class="action"><svg width="11" height="11" viewBox="0 0 12 12"><rect x="1" y="2" width="8" height="9" fill="none" stroke="#333"/><path d="M5 7l6-6" stroke="#333" stroke-width="1.5"/></svg></span></li>
      <li><span class="check done"></span>Verify your payment address<span class="action"><svg width="11" height="11" viewBox="0 0 12 12"><rect x="1" y="2" width="8" height="9" fill="none" stroke="#333"/><path d="M5 7l6-6" stroke="#333" stroke-width="1.5"/></svg></span></li>
      <li><span class="check done"></span>Visit the Jobs Board<span class="action"><svg width="11" height="11" viewBox="0 0 12 12"><rect x="1" y="2" width="8" height="9" fill="none" stroke="#333"/><path d="M5 7l6-6" stroke="#333" stroke-width="1.5"/></svg></span></li>
      <li><span class="check"></span>Add your profile pic<span class="action btn-complete">Complete</span></li>
      <li><span class="check done"></span>Add an about me to your profile<span class="action"><svg width="11" height="11" viewBox="0 0 12 12"><rect x="1" y="2" width="8" height="9" fill="none" stroke="#333"/><path d="M5 7l6-6" stroke="#333" stroke-width="1.5"/></svg></span></li>
      <li><span class="check"></span>Review and accept the PixelHarbor quality standards<span class="action btn-complete">Complete</span></li>
      <li><span class="check"></span>Submit your first design<span class="action btn-complete">Complete</span></li>
    </ul>
  </section>

  <div class="columns">
    <section class="panel col">
      <h3 class="section-head">Recommended Jobs</h3>
      <p class="section-intro">There are 12 jobs waiting for you to bid on that match your skills.</p>
      <div class="job"><span class="job-dot"></span><div><div class="job-title">Lorem ipsum is simply dummy text of the printing and typesetting industry.</div><div class="job-meta">5 Days Left &nbsp;|&nbsp; 0 &nbsp;|&nbsp; $150 &nbsp;|&nbsp; Watchlist</div></div></div>
      <div class="job"><span class="job-dot"></span><div><div class="job-title">Lorem ipsum is simply dummy text of the printing and typesetting industry.</div><div class="job-meta">5 Days Left &nbsp;|&nbsp; 0 &nbsp;|&nbsp; $150 &nbsp;|&nbsp; Watchlist</div></div></div>
      <div class="job"><span class="job-dot"></span><div><div class="job-title">Lorem ipsum is simply dummy text of the printing and typesetting industry.</div><div class="job-meta">5 Days Left &nbsp;|&nbsp; 0 &nbsp;|&nbsp; $150 &nbsp;|&nbsp; Watchlist</div></div></div>
      <div class="job"><span class="job-dot"></span><div><div class="job-title">Lorem ipsum is simply dummy text of the printing and typesetting industry.</div><div class="job-meta">5 Days Left &nbsp;|&nbsp; 0 &nbsp;|&nbsp; $150 &nbsp;|&nbsp; Watchlist</div></div></div>
      <div class="pager"><span>Page 4</span><span><b>‹ Previous</b> <b>Next ›</b></span></div>
    </section>
    <section class="panel col">
      <h3 class="section-head">Achievements</h3>
      <p class="section-intro">Earn PixelHarbor achievements as you unlock new milestones.</p>
      <div class="achievement"><span class="badge"></span><div><div class="ach-title">Double Blind</div><div class="ach-note">Submit at least 1 design to a contest.</div></div></div>
      <div class="achievement"><span class="badge"></span><div><div class="ach-title">Double Blind</div><div class="ach-note">Submit at least 1 design to a contest.</div></div></div>
      <div class="achievement"><span class="badge"></span><div><div class="ach-title">Double Blind</div><div class="ach-note">Submit at least 1 design to a contest.</div></div></div>
      <div class="achievement"><span class="badge"></span><div><div class="ach-title">Double Blind</div><div class="ach-note">Submit at least 1 design to a contest.</div></div></div>
    </section>
  </div>
</main>

<footer class="site-footer">
  <div class="footer-inner">
    <div class="footer-col links"><h4>I need a...</h4><ul><li>Logo Design</li><li>Website Design</li><li>Business Cards</li><li>Brochure Design</li><li>Banner Ads</li><li>T-Shirt Design</li><li>Packaging</li><li>Stationery</li></ul></div>
    <div class="footer-col links"><h4>Find a...</h4><ul><li>Logo Designers</li><li>Web Designers</li><li>Graphic Designers</li><li>Illustrators</li><li>Print Designers</li><li>Freelancers</li><li>Design Studios</li></ul></div>
    <div class="footer-col links"><h4>About us</h4><ul><li>Our Story</li><li>How it Works</li><li>Pricing</li><li>Blog</li><li>Careers</li><li>Contact Us</li><li>Help Centre</li></ul></div>
    <div class="footer-col"><h4>Popular pages</h4><div class="tags"><span>Design Contests</span><span>Logo Contests</span><span>Web Jobs</span><span>Print</span><span>Apparel</span><span>Branding</span><span>Icons</span><span>Flyers</span><span>Posters</span><span>Menus</span></div></div>
    <div class="footer-col subscribe"><h4>Subscribe to our newsletter</h4>
      <div class="subscribe-field"><div></div><span></span></div>
      <div class="social"><i></i><i></i><i></i><i></i></div>
      <div class="flags"><i></i><i></i><i></i><i></i></div>
      <div class="footer-brand"><i></i>PixelHarbor</div>
    </div>
  </div>
  <div class="footer-base">Copyright © PixelHarbor. All rights reserved. Terms of Use | Privacy Policy</div>
</footer>

</body>
</html>
```